Business Card Design - Local Discount Club

Looking for a fun business card for a local discount club. One side should be the logo only and the other should be have :

Name
Title
Phone, Email
Website

```html
<!DOCTYPE html>
<html lang="en">
<head>
<meta charset="utf-8">
<title>Dune Harbor Pass – Business Card</title>
<link rel="stylesheet" href="https://fonts.googleapis.com/css2?family=Montserrat:wght@400;500;800&display=swap">
<style>
  :root {
    --backdrop: #d4d4d4;
    --card: #000000;
    --edge: #3a5ad0;
    --brand-blue: #3b5fcc;
    --aqua: #35c6e0;
    --divider: #138a9a;
    --ink: #f2f2f2;
  }
  * { box-sizing: border-box; margin: 0; padding: 0; }
  html, body {
    width: 1200px; height: 913px; overflow: hidden;
    background: var(--backdrop);
    font-family: "Montserrat", Arial, sans-serif;
  }
  .sheet {
    width: 1200px; height: 913px;
    display: flex; align-items: center; justify-content: center; gap: 40px;
  }
  .card {
    position: relative;
    width: 560px; height: 320px;
    background: var(--card);
    border: 2px solid var(--edge);
  }
  .brand {
    display: flex; align-items: center; gap: 12px;
    color: var(--brand-blue);
    font-weight: 800;
    text-transform: uppercase;
    line-height: 1;
    white-space: nowrap;
  }
  .brand-dot {
    flex: none; border-radius: 50%; background: var(--aqua);
  }
  .card-back { display: flex; align-items: center; justify-content: center; }
  .card-back .brand { font-size: 40px; }
  .card-back .brand-dot { width: 22px; height: 22px; }

  .card-front .brand {
    position: absolute; left: 26px; top: 50%; transform: translateY(-50%);
    font-size: 17px; gap: 8px;
  }
  .card-front .brand-dot { width: 11px; height: 11px; }
  .divider {
    position: absolute; left: 262px; top: 42px; width: 2px; height: 236px;
    background: var(--divider);
  }
  .details { position: absolute; left: 290px; top: 56px; color: var(--ink); }
  .person-name {
    color: var(--brand-blue); font-weight: 800; font-size: 24px; letter-spacing: -0.5px;
  }
  .person-title { font-size: 14px; margin: 4px 0 14px; }
  .contact-list { list-style: none; font-size: 14px; }
  .contact-list li { display: flex; align-items: center; gap: 10px; margin-bottom: 8px; }
  .contact-icon { width: 16px; height: 16px; flex: none; }
  .address { font-size: 14px; line-height: 1.4; margin-top: 6px; padding-left: 26px; }
</style>
</head>
<body>
<main class="sheet">
  <section class="card card-front" aria-label="Card front with contact details">
    <div class="brand"><span class="brand-dot"></span>Dune Harbor Pass</div>
    <div class="divider"></div>
    <div class="details">
      <h1 class="person-name">MARCUS ELLERY</h1>
      <p class="person-title">Managing Director</p>
      <ul class="contact-list">
        <li>
          <svg class="contact-icon" viewBox="0 0 16 16" aria-hidden="true"><circle cx="8" cy="8" r="8" fill="var(--aqua)"/><path d="M5 4.5l1.6-.5 1 2-1 .8a5 5 0 0 0 2.6 2.6l.8-1 2 1-.5 1.6c-3.6.3-6.8-2.9-6.5-6.5z" fill="#000"/></svg>
          000-000-0000
        </li>
        <li>
          <svg class="contact-icon" viewBox="0 0 16 16" aria-hidden="true"><circle cx="8" cy="8" r="8" fill="var(--aqua)"/><rect x="4" y="5" width="8" height="6" fill="#000"/><path d="M4 5l4 3.2L12 5" stroke="var(--aqua)" stroke-width="1" fill="none"/></svg>
          hello@duneharbor.com
        </li>
        <li>
          <svg class="contact-icon" viewBox="0 0 16 16" aria-hidden="true"><circle cx="8" cy="8" r="8" fill="var(--aqua)"/><circle cx="8" cy="8" r="4.2" fill="none" stroke="#000" stroke-width="1.2"/><path d="M3.8 8h8.4M8 3.8c-2 2.4-2 6 0 8.4M8 3.8c2 2.4 2 6 0 8.4" stroke="#000" stroke-width="1" fill="none"/></svg>
          www.duneharborpass.com
        </li>
      </ul>
      <p class="address">421, Address line here<br>Country Name, 45452</p>
    </div>
  </section>

  <section class="card card-back" aria-label="Card back with brand name">
    <div class="brand"><span class="brand-dot"></span>Dune Harbor Pass</div>
  </section>
</main>
</body>
</html>
```